Small rum distillery looking for bottle design

Small rum distillery in Estonia. Looking for bottle lable design. It should be simple but at the same time point out from the variety of other bottles.
As we are a small nordic country, design can be some how nordic or represent our country. It can also have some connection with sailing or sea as we know it pirates love it.
Bottle we are using is Corvane 540

Industry/Entity Type

food and beverage

Other font styles liked:
• Baskerville

```html
<!DOCTYPE html>
<html lang="en">
<head>
<meta charset="utf-8">
<title>Harkmoor Distillery Rum Label</title>
<link rel="stylesheet" href="https://fonts.googleapis.com/css2?family=Libre+Baskerville:wght@400;700&family=Alfa+Slab+One&family=PT+Sans+Narrow:wght@400;700&display=swap">
<style>
  :root {
    --bg: #0c0c0c;
    --label-red: #b24a48;
    --label-red-dark: #8c3433;
    --paper: #f1efec;
    --ink: #4a4a4a;
    --ink-dark: #2f2f2f;
    --wreath: #9c9c9c;
  }
  html, body {
    margin: 0;
    padding: 0;
    width: 1200px;
    height: 1200px;
    overflow: hidden;
    background: var(--bg);
  }
  .label-canvas {
    display: block;
    width: 1200px;
    height: 1200px;
  }
  .label-border { fill: var(--label-red); }
  .label-paper { fill: var(--paper); }
  .label-rule { fill: none; stroke: var(--label-red); stroke-width: 3; }
  .ribbon { fill: var(--label-red); }
  .ribbon-fold { fill: var(--label-red-dark); }
  .medallion-wreath { fill: url(#wreathTone); }
  .medallion-ring { fill: none; stroke: var(--label-red); stroke-width: 8; }
  .medallion-face { fill: var(--paper); }
  .brand-name { fill: var(--ink); font-family: "Libre Baskerville", serif; font-weight: 400; font-size: 27px; }
  .brand-sub { fill: var(--ink); font-family: "Libre Baskerville", serif; font-weight: 400; font-size: 14px; letter-spacing: 6px; }
  .brand-rule { stroke: var(--ink); stroke-width: 1.5; }
  .brand-dot { fill: none; stroke: var(--ink); stroke-width: 2; }
  .product-name {
    font-family: "Alfa Slab One", serif;
    font-size: 160px;
    fill: var(--label-red);
    stroke: var(--label-red-dark);
    stroke-width: 3;
    letter-spacing: 2px;
  }
  .tagline {
    font-family: "PT Sans Narrow", sans-serif;
    font-weight: 700;
    font-size: 27px;
    fill: var(--ink);
    letter-spacing: 0.5px;
  }
  .badge-wreath { fill: none; stroke: var(--wreath); stroke-width: 10; stroke-dasharray: 4 3; }
  .badge-ring { fill: var(--paper); stroke: var(--label-red); stroke-width: 5; }
  .badge-caption { font-family: "PT Sans Narrow", sans-serif; font-weight: 700; font-size: 19px; fill: var(--ink); }
  .badge-value { font-family: "PT Sans Narrow", sans-serif; font-size: 44px; }
  .badge-value.dark { fill: var(--ink); }
  .badge-value.red { fill: var(--label-red); }
  .established { font-family: "PT Sans Narrow", sans-serif; font-size: 36px; fill: var(--ink); }
  .established .year { fill: var(--label-red); font-size: 42px; }
  .illustration { fill: url(#engravingTone); }
</style>
</head>
<body>
<svg class="label-canvas" viewBox="0 0 1200 1200" xmlns="http://www.w3.org/2000/svg">
  <defs>
    <radialGradient id="wreathTone" cx="50%" cy="50%" r="50%">
      <stop offset="70%" stop-color="#d6d6d6"/>
      <stop offset="100%" stop-color="#8a8a8a"/>
    </radialGradient>
    <linearGradient id="engravingTone" x1="0" y1="0" x2="1" y2="1">
      <stop offset="0%" stop-color="#c9c9c9"/>
      <stop offset="60%" stop-color="#9a9a9a"/>
      <stop offset="100%" stop-color="#7a7a7a"/>
    </linearGradient>
  </defs>

  <g class="label-body">
    <path class="label-border" d="M270,300 H930 A40,40 0 0 0 970,340 V1040 A40,40 0 0 0 930,1080 H270 A40,40 0 0 0 230,1040 V340 A40,40 0 0 0 270,300 Z"/>
    <path class="label-paper" d="M282,316 H918 A36,36 0 0 0 954,352 V1028 A36,36 0 0 0 918,1064 H282 A36,36 0 0 0 246,1028 V352 A36,36 0 0 0 282,316 Z"/>
    <path class="label-rule" d="M292,332 H908 A30,30 0 0 0 938,362 V1018 A30,30 0 0 0 908,1048 H292 A30,30 0 0 0 262,1018 V362 A30,30 0 0 0 292,332 Z"/>
  </g>

  <g class="ribbons">
    <path class="ribbon-fold" d="M250,300 L300,260 L320,330 Z"/>
    <path class="ribbon" d="M300,250 Q430,200 500,260 L500,330 Q430,280 320,330 Z"/>
    <path class="ribbon-fold" d="M950,300 L900,260 L880,330 Z"/>
    <path class="ribbon" d="M900,250 Q770,200 700,260 L700,330 Q770,280 880,330 Z"/>
  </g>

  <g class="medallion">
    <circle class="medallion-wreath" cx="600" cy="315" r="150" role="img" aria-label="Engraved wreath of oak leaves and rope around the medallion"/>
    <circle class="medallion-ring" cx="600" cy="315" r="118"/>
    <circle class="medallion-face" cx="600" cy="315" r="112"/>
    <circle class="brand-dot" cx="600" cy="262" r="20"/>
    <text class="brand-name" x="600" y="325" text-anchor="middle">HARKMOOR</text>
    <line class="brand-rule" x1="528" y1="338" x2="672" y2="338"/>
    <text class="brand-sub" x="603" y="362" text-anchor="middle">DISTILLERY</text>
  </g>

  <text class="product-name" x="292" y="622">RUM</text>
  <text class="tagline" x="296" y="660">SMALL RUM DISTILLERY IN ESTONIA</text>

  <path class="illustration" role="img" aria-label="Engraved illustration of a tall sailing ship with an anchor and rope in the foreground"
        d="M640,690 H930 V1030 H280 V905 H640 Z"/>

  <g class="badge badge-abv">
    <circle class="badge-wreath" cx="350" cy="765" r="68"/>
    <circle class="badge-ring" cx="350" cy="765" r="54"/>
    <text class="badge-caption" x="350" y="750" text-anchor="middle">ALC/VOL</text>
    <text class="badge-value dark" x="350" y="795" text-anchor="middle">46%</text>
  </g>
  <g class="badge badge-batch">
    <circle class="badge-wreath" cx="530" cy="765" r="68"/>
    <circle class="badge-ring" cx="530" cy="765" r="54"/>
    <text class="badge-caption" x="530" y="750" text-anchor="middle">BATCH NO</text>
    <text class="badge-value red" x="530" y="795" text-anchor="middle">002</text>
  </g>

  <text class="established" x="290" y="878">EST'D <tspan class="year">2015</tspan></text>
</svg>
</body>
</html>
```